I need a business card design for a new company that will be doing consulting work around issues of cultural competency, and diversity and inclusion. I would like the design to be crisp and clear with bold but conservative colors and incorporate shades of blue

Target Market(s)

Small businesses, schools, non-profits

Industry/Entity Type

Consulting

Font styles to use
Serif
Sans Serif

Colors
0c5ba6
6b449b
3276b5
0292cd

Requirements
Must have
• A Morrow Venture (name of company)
• Lemlem Tavish
• CEO
• lemlem@amorrowventure.com
• (215)483-2756

```html
<!DOCTYPE html>
<html lang="en">
<head>
<meta charset="utf-8">
<title>A Morrow Venture – Business Card</title>
<link href="https://fonts.googleapis.com/css2?family=Raleway:wght@300;400;600&display=swap" rel="stylesheet">
<style>
  :root {
    --card-blue: #1a94d0;
    --paper: #ffffff;
    --ink-light: #ffffff;
  }
  html, body {
    margin: 0;
    padding: 0;
    overflow: hidden;
    background: var(--paper);
  }
  .card {
    position: relative;
    width: 1200px;
    height: 686px;
    background: var(--paper);
    overflow: hidden;
    font-family: "Raleway", Arial, sans-serif;
  }
  .card__panel {
    position: absolute;
    inset: 0;
    width: 1200px;
    height: 686px;
  }
  .card__panel polygon { fill: var(--card-blue); }

  .brand {
    position: absolute;
    left: 88px;
    top: 318px;
    margin: 0;
    color: var(--card-blue);
    font-weight: 400;
    font-size: 46px;
    line-height: 1;
    white-space: nowrap;
  }

  .contact {
    position: absolute;
    left: 683px;
    top: 0;
    color: var(--ink-light);
    line-height: 1;
  }
  .contact > * {
    position: absolute;
    left: 0;
    margin: 0;
    white-space: nowrap;
  }
  .contact__name {
    top: 228px;
    font-size: 54px;
    font-weight: 600;
    letter-spacing: 2px;
  }
  .contact__role {
    top: 293px;
    font-size: 34px;
    font-weight: 300;
  }
  .contact__email {
    top: 369px;
    font-size: 27px;
    font-weight: 300;
    letter-spacing: 0.3px;
  }
  .contact__phone {
    top: 420px;
    font-size: 27px;
    font-weight: 300;
    letter-spacing: 0.3px;
  }
</style>
</head>
<body>
<main class="card">
  <svg class="card__panel" viewBox="0 0 1200 686" aria-hidden="true">
    <polygon points="600,0 1200,0 1200,686 600,686 600,614 577,614 577,485 600,485 600,199 626,199 626,71 600,71"/>
  </svg>

  <p class="brand">A Morrow Venture</p>

  <section class="contact">
    <h1 class="contact__name">LEMLEM TAVISH</h1>
    <p class="contact__role">CEO</p>
    <p class="contact__email">lemlem@amorrowventure.com</p>
    <p class="contact__phone">(215)483-2756</p>
  </section>
</main>
</body>
</html>
```